Visitenkarten-Design für  Softwareunternehmen
Visitenkarten-Design für Softwareunternehmen
Zielgruppe
Wir sind ein B2B Softwareunternehmen, das eine Energiemonitoringsoftware für die mittelständische Industrie entwickelt hat. Das heißt unsere Visitenkarten werden überwiegend an unsere Zielgruppe, d.h. Geschäftsführer produzierender mittelständischer Industrie ausgehändigt.
Aufgabenstellung
Gleichzeitig treten wir nach außen jung, innovativ und voller Tatendrang auf. Ganz nach unserer Vision: Voll Energie. Null Emission. (Auch gerne auf der Visitenkarte mit aufnehmen). Uns ist es wichtig, unser CI nach außen zu kommunizieren und unsere Webseite auf der Visitenkarte zu platzieren.
Die Visitenkarte soll einzeln für jeden MitarbeiterIn personalisiert werden können.

```html
<!DOCTYPE html>
<html lang="de">
<head>
<meta charset="utf-8">
<title>Visitenkarte – Voltara</title>
<link rel="stylesheet" href="https://fonts.googleapis.com/css2?family=Roboto:ital,wght@0,300;0,400;0,700;1,700&display=swap">
<style>
  :root {
    --stage: #2b3536;
    --card-dark: #354244;
    --card-light: #ffffff;
    --ink: #2c3638;
    --ink-soft: #3a4547;
    --paper-text: #ffffff;
  }
  * { box-sizing: border-box; margin: 0; padding: 0; }
  html, body {
    width: 1200px; height: 800px; overflow: hidden;
    background: var(--stage);
    font-family: "Roboto", sans-serif;
  }
  .stage {
    position: relative; width: 1200px; height: 800px;
    display: flex; align-items: center; justify-content: center; gap: 60px;
  }
  .card {
    width: 420px; height: 420px; border-radius: 40px;
    position: relative;
  }
  .card--front {
    background: var(--card-light);
    color: var(--ink);
    display: flex; flex-direction: column; align-items: center;
    padding-top: 52px;
  }
  .person__name { font-size: 30px; font-weight: 700; letter-spacing: -0.3px; }
  .person__role { font-size: 24px; font-weight: 300; margin-top: 6px; color: var(--ink-soft); }
  .divider { width: 36px; height: 3px; background: var(--ink); margin: 30px 0 34px; }
  .address { font-size: 19px; font-weight: 400; text-align: center; line-height: 1.4; color: var(--ink-soft); }
  .contact { margin-top: 26px; font-size: 19px; line-height: 1.55; color: var(--ink-soft); }
  .contact__label { font-weight: 700; color: var(--ink); display: inline-block; width: 34px; }
  .card--back {
    background: var(--card-dark);
    color: var(--paper-text);
    border: 1px solid #3f4d4f;
  }
  .brand {
    position: absolute; top: 150px; left: 0; right: 0;
    text-align: center; font-size: 58px; font-weight: 700; letter-spacing: 6px;
  }
  .web {
    position: absolute; bottom: 58px; left: 0; right: 0;
    text-align: center; font-size: 21px; font-weight: 700; font-style: italic;
  }
</style>
</head>
<body>
  <main class="stage">
    <section class="card card--front">
      <h1 class="person__name">Lena Brauner</h1>
      <p class="person__role">Leiterin Marketing</p>
      <div class="divider"></div>
      <p class="address">Lindenweg 8<br>88212 Ravensburg</p>
      <div class="contact">
        <p><span class="contact__label">T :</span>0751 362 14 90</p>
        <p><span class="contact__label">M :</span>hallo@voltara.de</p>
        <p><span class="contact__label">W :</span>www.voltara.de</p>
      </div>
    </section>
    <section class="card card--back">
      <p class="brand">VOLTARA</p>
      <p class="web">www.voltara-energie.de</p>
    </section>
  </main>
</body>
</html>
```